Home page in PSD needed for a Business Consultant website

We have been given the mandate to re-do the website: http://www.lumivanconseil.ca/

Deliverable: home page in PSD format in French language

Context: Luc Dorval is a business strategist specializing in marketing, creativity, business development. He helps small and medium companies develop their business through creative marketing strategies.

Some websites we like for your inspiration:

http://www.tallpinegrove.com.au/
http://www.trwadvisory.com.au/
http://fjalladvisors.com.au/
http://www.olubrenix.com/fr

Target Market(s)

B2B: Companies looking on the web for a business consultant who can help them with marketing, business developement, printing needs.

Industry/Entity Type

Business

Requirements
Must have
• Call to action: "Simplifiez votre développement des affaires" (which means "Simplify your business development")
• List of services (main menu)
• Marketing
• Développement des affaires
• Créativité
• Scolaire
• Impression
• Top menu as follow:
• Accueil
• À propos
• Contact

```html
<!DOCTYPE html>
<html lang="fr">
<head>
<meta charset="utf-8">
<title>Lumivan Conseil — Accueil</title>
<link rel="stylesheet" href="https://fonts.googleapis.com/css2?family=Arimo:ital,wght@0,400;0,700;1,400&display=swap">
<style>
  :root {
    --blue: #0a7cc8;
    --text: #444444;
    --text-muted: #555555;
    --nav-grey: #5a5a5a;
    --light-bg: #f2f2f2;
    --btn-grey: #e8e8e8;
    --footer-bg: #3a3939;
    --footer-text: #ffffff;
    --footer-muted: #c9c9c9;
    --divider: #d8d8d8;
    --white: #ffffff;
  }
  * { box-sizing: border-box; margin: 0; padding: 0; }
  html, body { width: 1168px; height: 1200px; overflow: hidden; }
  body {
    position: relative;
    background: var(--white);
    font-family: "Arimo", Arial, sans-serif;
    color: var(--text);
  }
  .abs { position: absolute; }

  /* Header */
  .top-rule { left: 0; top: 0; width: 1168px; height: 4px; background: var(--blue); }
  .site-header { left: 0; top: 4px; width: 1168px; height: 152px; border-bottom: 1px solid #eeeeee; }
  .brand { left: 112px; top: 38px; display: flex; align-items: center; gap: 10px; }
  .brand-mark { width: 14px; height: 14px; border-radius: 50%; background: var(--blue); }
  .brand-name { font-size: 32px; font-weight: 400; color: #2b2b2b; letter-spacing: 0.5px; }
  .brand-tagline { left: 144px; top: 90px; font-size: 10px; letter-spacing: 1.6px; color: #555; }
  .brand-tagline .sep { color: var(--blue); padding: 0 4px; }

  .utility-nav { right: 300px; top: 32px; display: flex; font-size: 11px; font-weight: 700; letter-spacing: 0.4px; }
  .utility-nav a { color: #8a8a8a; text-decoration: none; padding: 0 8px; border-left: 1px solid var(--divider); line-height: 13px; }
  .utility-nav a:first-child { border-left: 0; }
  .utility-nav a.is-active { color: var(--blue); }

  .contact { left: 907px; top: 22px; display: flex; gap: 12px; align-items: center; }
  .contact-name { font-size: 15px; color: var(--blue); line-height: 17px; }
  .contact-phone { font-size: 15px; font-weight: 700; color: var(--nav-grey); line-height: 17px; }

  .main-nav { right: 130px; top: 79px; display: flex; font-size: 13px; font-weight: 700; letter-spacing: 0.2px; }
  .main-nav a { color: var(--nav-grey); text-decoration: none; padding: 0 9px; border-left: 1px solid var(--divider); line-height: 17px; }
  .main-nav a:first-child { border-left: 0; }
  .main-nav a:last-child { padding-right: 0; }

  /* Hero */
  .hero { left: 0; top: 156px; width: 1168px; height: 356px;
    background: linear-gradient(180deg, #eef4f9 0%, #f8fbfd 45%, #ffffff 70%, #eef0f2 100%); }
  .hero-intro { right: 675px; top: 80px; font-size: 20px; color: #3a3a3a; text-align: right; }
  .hero-title { right: 675px; top: 112px; font-size: 29px; font-weight: 400; color: var(--blue); line-height: 39px; text-align: right; }
  .hero-cta { right: 675px; top: 248px; height: 36px; padding: 0 13px; background: var(--blue); color: var(--white);
    border-radius: 3px; font-size: 15px; display: flex; align-items: center; gap: 12px; white-space: nowrap; }
  .hero-photo { left: 540px; top: 28px; width: 510px; height: 328px;
    background: linear-gradient(180deg, #d9dde2 0%, #8a9098 55%, #3c4046 100%); }
  .slider-dots { left: 579px; top: 341px; display: flex; gap: 3px; }
  .slider-dots span { width: 11px; height: 8px; background: #cfcfcf; }

  /* Band */
  .quote-band { left: 0; top: 512px; width: 1168px; height: 125px; background: var(--blue);
    color: var(--white); font-size: 19px; line-height: 30px; text-align: center; padding-top: 27px; }

  /* Services */
  .service { top: 637px; width: 270px; text-align: center; }
  .service h2 { margin-top: 45px; font-size: 15px; font-weight: 700; color: var(--blue); letter-spacing: 0.3px; }
  .service p { margin-top: 26px; font-size: 12px; line-height: 19px; color: var(--text-muted); }
  .service .btn-more { display: inline-block; margin-top: 24px; width: 90px; height: 27px; line-height: 27px;
    background: var(--btn-grey); color: var(--blue); font-size: 13px; }

  /* Testimonial */
  .testimonial { left: 0; top: 887px; width: 1168px; height: 161px; background: var(--light-bg); border-top: 1px solid #e4e4e4; }
  .client-photo { left: 154px; top: 33px; width: 111px; height: 111px; border-radius: 50%;
    background: radial-gradient(circle at 50% 40%, #c9cfd6 0%, #7d8794 60%, #2e3a52 100%); border: 3px solid #e6e6e6; }
  .testimonial h3 { left: 308px; top: 30px; font-size: 14px; font-weight: 700; color: var(--blue); letter-spacing: -0.2px; }
  .testimonial blockquote { left: 308px; top: 66px; width: 670px; font-size: 11.6px; line-height: 20px; font-style: italic; color: var(--text-muted); }
  .testimonial-arrows { left: 1001px; top: 24px; }

  /* Footer */
  .site-footer { left: 0; top: 1048px; width: 1168px; height: 152px; background: var(--footer-bg); }
  .footer-nav { left: 118px; top: 38px; display: flex; font-size: 14px; font-weight: 700; }
  .footer-nav a { color: var(--footer-text); text-decoration: none; padding: 0 9px; border-left: 1px solid #5a5a5a; line-height: 17px; }
  .footer-nav a:first-child { border-left: 0; padding-left: 5px; }
  .copyright { left: 119px; top: 82px; font-size: 12px; color: var(--footer-muted); }
  .newsletter-label { right: 129px; top: 40px; font-size: 12px; font-weight: 700; color: var(--footer-text); letter-spacing: 0.2px; }
  .newsletter-field { left: 816px; top: 56px; width: 186px; height: 34px; background: var(--white);
    font-size: 12px; color: #444; padding: 11px 10px; }
  .newsletter-go { left: 1002px; top: 56px; width: 37px; height: 34px; background: var(--blue); color: var(--white);
    font-size: 15px; display: flex; align-items: center; justify-content: center; }
  .social { top: 101px; width: 26px; height: 26px; border-radius: 2px; }
  .social--one { left: 983px; background: #3b5a9a; }
  .social--two { left: 1013px; background: #1a8fd0; }
</style>
</head>
<body>
  <div class="abs top-rule"></div>

  <header class="abs site-header">
    <div class="abs brand">
      <span class="brand-mark"></span>
      <span class="brand-name">Lumivan Conseil</span>
    </div>
    <div class="abs brand-tagline">commercialisation<span class="sep">|</span>marketing<span class="sep">|</span>créativité</div>

    <nav class="abs utility-nav">
      <a href="#" class="is-active">ACCUEIL</a>
      <a href="#">À PROPOS</a>
      <a href="#">CONTACT</a>
    </nav>

    <div class="abs contact">
      <svg width="26" height="26" viewBox="0 0 26 26" aria-hidden="true">
        <circle cx="13" cy="13" r="11.5" fill="none" stroke="#8a8a8a" stroke-width="1.6"/>
        <path d="M9 7.5c-1 .6-1.6 1.6-1.2 3 .9 3 3.6 6 6.6 7.4 1.3.6 2.5.1 3.2-.8l-2.2-2-1.3.9c-1.4-.7-2.8-2.2-3.4-3.6l1-1.2z" fill="#8a8a8a"/>
      </svg>
      <div>
        <div class="contact-name">Luc Dorval</div>
        <div class="contact-phone">514 555 0182</div>
      </div>
    </div>

    <nav class="abs main-nav">
      <a href="#">MARKETING</a>
      <a href="#">DÉVELOPPEMENT DES AFFAIRES</a>
      <a href="#">CRÉATIVITÉ</a>
      <a href="#">SCOLAIRE</a>
      <a href="#">IMPRESSION</a>
    </nav>
  </header>

  <section class="abs hero">
    <p class="abs hero-intro">Votre guichet unique pour vos</p>
    <h1 class="abs hero-title">besoins en vente, marketing<br>et commercialisation!</h1>
    <a class="abs hero-cta">Simplifiez votre développement des affaires <span>»</span></a>
    <div class="abs hero-photo" role="img" aria-label="Photo de trois professionnels souriants en tenue d'affaires, pouces levés"></div>
    <div class="abs slider-dots"><span></span><span></span><span></span><span></span><span></span></div>
  </section>

  <section class="abs quote-band">
    Même avec les meilleurs outils de vente,un bon vendeur qui n'est pas formé<br>ne pourra être performant à 100% !
  </section>

  <section class="abs service" style="left:110px">
    <h2>COMMERCIALISATION</h2>
    <p>Lorem Ipsum is simply dummy text of the printing<br>and typesetting industry Ipsum has been the<br>industry's dummy text ever.</p>
    <a class="btn-more">Read more</a>
  </section>
  <section class="abs service" style="left:442px">
    <h2>MARKETING</h2>
    <p>Lorem Ipsum is simply dummy text of the printing<br>and typesetting industry Ipsum has been the<br>industry's dummy text ever.</p>
    <a class="btn-more">Read more</a>
  </section>
  <section class="abs service" style="left:756px">
    <h2>CREATIVITE</h2>
    <p>Lorem Ipsum is simply dummy text of the printing<br>and typesetting industry Ipsum has been the<br>industry's dummy text ever.</p>
    <a class="btn-more" style="margin-top:22px">Read more</a>
  </section>

  <section class="abs testimonial">
    <div class="abs client-photo" role="img" aria-label="Portrait d'un client"></div>
    <h3 class="abs">CLIENT FEEBACK</h3>
    <blockquote class="abs">Lorem ipsum dolor sit amet, consectetur adipisicing elit, sed do eiusmod tempor incididunt ut labore et dolore magna aliqua.<br>Ut enim ad minim veniam, quis nostrud exercitation ullamco laboris nisi ut aliquip ex ea commodo consequat. Duis aute irure<br>dolor in reprehenderit in voluptate velit esse cillum dolore eu fugiat nulla pariatur.</blockquote>
    <svg class="abs testimonial-arrows" width="32" height="16" viewBox="0 0 32 16" aria-hidden="true">
      <path d="M10 2 L3 8 L10 14" fill="none" stroke="#b5b5b5" stroke-width="3"/>
      <path d="M21 2 L28 8 L21 14" fill="none" stroke="#b5b5b5" stroke-width="3"/>
    </svg>
  </section>

  <footer class="abs site-footer">
    <nav class="abs footer-nav">
      <a href="#">ACCUEIL</a>
      <a href="#">COMMERCIALISATION</a>
      <a href="#">MARKETING</a>
      <a href="#">CRÉATIVITÉ</a>
    </nav>
    <p class="abs copyright">© Lumivan Conseil 2013. Tous droits réservés</p>
    <p class="abs newsletter-label">INSCRIVEZ-VOUS À NOTRE NEWSLETTER!</p>
    <div class="abs newsletter-field">Votre courrie!</div>
    <div class="abs newsletter-go">Go</div>
    <span class="abs social social--one" aria-label="Réseau social"></span>
    <span class="abs social social--two" aria-label="Réseau social"></span>
  </footer>
</body>
</html>
```